Concrete Grinding and Polishing company business card with logo, based in Australia.

We need a business card design along with logo for a new company based in Melbourne called BrightLap. We specialise in the grinding and polishing of concrete. Polished concrete is durable, easy to maintain, cost effective, dust proof, has increased light reflectivity, and is slip resistant, among other benefits. In short, polished concrete is a popular flooring solution because of its practical advantages, as well as it's decorative appeal.

Industry/Entity Type

Business

Requirements
Must have
• It must have the company name(BrightLap) as well as the slogan: A Cut Above The Rest.
Nice to have
• Something that symbolises polished concrete. Would also like it to have a silver background with black writing, if possible.

```html
<!DOCTYPE html>
<html lang="en">
<head>
<meta charset="utf-8">
<title>BrightLap – Business Card</title>
<link rel="stylesheet" href="https://fonts.googleapis.com/css2?family=PT+Sans+Narrow:wght@400;700&display=swap">
<style>
  :root {
    --backdrop: #2b2b2b;
    --card-dark: #4b4b4b;
    --card-dark-edge: #3f3f3f;
    --card-light: #f4f4f4;
    --card-light-edge: #dcdcdc;
    --ink-light: #ffffff;
    --ink-soft: #c9c9c9;
    --ink-dark: #3a3a3a;
    --ink-mid: #5a5a5a;
    --art-glow: #f7f7f7;
    --art-shade: #b9b9b9;
    --font-main: "PT Sans Narrow", "Arial Narrow", sans-serif;
  }

  html, body {
    margin: 0;
    padding: 0;
    width: 935px;
    height: 1200px;
    overflow: hidden;
    background: var(--backdrop);
    font-family: var(--font-main);
  }

  .canvas {
    position: relative;
    width: 935px;
    height: 1200px;
  }

  /* ---------- Cards ---------- */
  .card {
    position: absolute;
    left: 157px;
    width: 620px;
    height: 354px;
    overflow: hidden;
    box-shadow: 0 6px 18px rgba(0, 0, 0, 0.45);
    background: linear-gradient(180deg, var(--card-light) 0%, var(--card-light-edge) 100%);
  }

  .card-band {
    position: absolute;
    left: 0;
    top: 0;
    width: 100%;
    background: linear-gradient(135deg, var(--card-dark) 0%, var(--card-dark-edge) 100%);
  }

  .card-front { top: 30px; }
  .card-front .card-band { height: 210px; }

  .card-back { top: 414px; }
  .card-back .card-band { height: 190px; }

  /* ---------- Artwork area ---------- */
  .artwork {
    position: absolute;
    background: radial-gradient(ellipse at 50% 85%, var(--art-glow) 0%, #e2e2e2 45%, var(--art-shade) 100%);
  }

  .card-front .artwork { left: 45px; top: 62px; width: 150px; height: 190px; }
  .card-back .artwork  { left: 250px; top: 36px; width: 120px; height: 150px; }
  .showcase-artwork    { left: 347px; top: 812px; width: 240px; height: 290px; }

  /* ---------- Name and slogan ---------- */
  .brand {
    position: absolute;
    display: flex;
    align-items: center;
    gap: 0.3em;
    margin: 0;
    font-weight: 700;
    line-height: 1;
    color: var(--ink-dark);
  }

  .brand-square {
    width: 0.45em;
    height: 0.45em;
    background: currentColor;
  }

  .slogan {
    position: absolute;
    margin: 0;
    font-weight: 400;
    line-height: 1;
    letter-spacing: 0.06em;
    color: var(--ink-mid);
    white-space: nowrap;
  }

  .card-front .brand  { left: 45px; top: 262px; font-size: 30px; }
  .card-front .slogan { left: 45px; top: 298px; font-size: 14px; }

  .card-back .brand  { left: 250px; top: 196px; font-size: 22px; }
  .card-back .slogan { left: 250px; top: 223px; font-size: 12px; }

  .showcase-brand  { left: 347px; top: 1114px; font-size: 42px; color: var(--ink-light); }
  .showcase-slogan { left: 347px; top: 1162px; font-size: 20px; color: var(--ink-soft); }

  /* ---------- Front card text ---------- */
  .contact {
    position: absolute;
    right: 36px;
    text-align: right;
    font-weight: 700;
    margin: 0;
  }

  .contact-name { top: 34px; font-size: 30px; line-height: 1; color: var(--ink-light); }
  .contact-role { top: 66px; font-size: 16px; color: var(--ink-soft); }
  .contact-lines { top: 120px; font-size: 16px; line-height: 1.3; color: var(--ink-light); }
  .contact-address { top: 228px; font-size: 15px; line-height: 1.35; color: var(--ink-dark); }
  .contact p { margin: 0; }

  /* ---------- Back card text ---------- */
  .back-web {
    position: absolute;
    left: 0;
    top: 262px;
    width: 100%;
    text-align: center;
    font-weight: 700;
    font-size: 26px;
    color: var(--ink-dark);
    margin: 0;
  }
</style>
</head>
<body>
<main class="canvas">

  <section class="card card-front" aria-label="Business card front">
    <div class="card-band"></div>
    <div class="artwork" role="img" aria-label="Illustration of a worker guiding a concrete floor grinder against a light sunburst"></div>
    <p class="brand"><span class="brand-square"></span>BrightLap</p>
    <p class="slogan">a cut above the rest</p>

    <h1 class="contact contact-name">Your Name</h1>
    <p class="contact contact-role">lorem ipsum</p>
    <div class="contact contact-lines">
      <p>tel: 123 456 789</p>
      <p>fax: 123 456 789</p>
      <p>email: yourname@brightlapfloors.com</p>
    </div>
    <div class="contact contact-address">
      <p>adress: lorem ipsum lorem ipsum lorem ipsum lorem ipsum</p>
      <p>web: www.brightlapfloors.com</p>
    </div>
  </section>

  <section class="card card-back" aria-label="Business card back">
    <div class="card-band"></div>
    <div class="artwork" role="img" aria-label="Illustration of a worker guiding a concrete floor grinder against a light sunburst"></div>
    <p class="brand"><span class="brand-square"></span>BrightLap</p>
    <p class="slogan">a cut above the rest</p>
    <p class="back-web">www.brightlapfloors.com</p>
  </section>

  <div class="artwork showcase-artwork" role="img" aria-label="Illustration of a worker guiding a concrete floor grinder against a light sunburst"></div>
  <p class="brand showcase-brand"><span class="brand-square"></span>BrightLap</p>
  <p class="slogan showcase-slogan">a cut above the rest</p>

</main>
</body>
</html>
```